Medical device company presentation

Traloma is an early stage medical device company. We are developing an Ultrasound based catheter to treat hypertension.
We'd like the presentation slides to be clean with green/blue colors (Attached is our Logo which should part of each slide).
Updates
Project Deadline Extended
Reason: I would like to receive more designs options.
I received only 3-4 good and full designs.
Target Market(s)
Medical device companies
Industry/Entity Type
It Company
Look and feel

```html
<!DOCTYPE html>
<html lang="en">
<head>
<meta charset="utf-8">
<title>Traloma Presentation Slides</title>
<link rel="stylesheet" href="https://fonts.googleapis.com/css2?family=Open+Sans:wght@400;600;700&display=swap">
<style>
:root{
  --green:#8cc63f;
  --green-d:#6aa52b;
  --blue:#1b96d3;
  --blue-d:#0e6fa8;
  --ink:#4a4a4a;
  --mute:#8d8d8d;
  --line:#e3e8ec;
  --soft:#f3f6f8;
}
*{box-sizing:border-box}
html,body{margin:0;width:1200px;height:3876px;overflow:hidden;background:#fff;font-family:'Open Sans',sans-serif}
.deck{display:grid;grid-template-columns:repeat(3,392px);grid-auto-rows:220px;gap:8px;padding:4px}
.slide{position:relative;overflow:hidden;background:#fff;box-shadow:0 0 0 1px #e4e7ea}
.slide.green{background:linear-gradient(135deg,#9ccf4e,#76b234)}
.abs{position:absolute}
.logo{position:absolute;top:7px;right:10px;font-size:9px;font-weight:700;color:var(--green);display:flex;align-items:center;gap:3px;z-index:2}
.logo::before{content:"";width:7px;height:7px;border-radius:50%;background:var(--blue)}
.logo.light{color:#fff}
.logo.light::before{background:#fff}
.hd{position:absolute;left:16px;top:14px;margin:0;font-size:14px;font-weight:600;color:var(--blue)}
.hd.white{color:#fff}
.ph{position:absolute;background:linear-gradient(135deg,#d6e1e8,#a9bbc8)}
.ph.g{background:linear-gradient(135deg,#a8d766,#6fae32)}
.ph.round{border-radius:50%}
.p{font-size:6px;line-height:1.55;color:var(--mute);margin:0}
.p.white{color:#eaf6dc}
.sub{font-size:7.5px;font-weight:700;color:var(--ink);margin:0 0 3px}
.sub.blue{color:var(--blue)}
.foot{position:absolute;left:0;right:0;bottom:0;height:3px;background:linear-gradient(90deg,var(--green),var(--blue))}
.li{display:flex;gap:5px;align-items:center;font-size:6px;color:var(--ink);margin:0 0 6px}
.li::before{content:"";width:8px;height:8px;border-radius:50%;background:var(--green);flex:none}
.li.blue::before{background:var(--blue)}
.chip{position:absolute;width:14px;height:14px;border-radius:3px;background:var(--blue)}
.circle{position:absolute;border-radius:50%;background:var(--blue)}
.panel{position:absolute;background:var(--green)}
.cap{font-size:6px;color:var(--ink);text-align:center;margin:3px 0 0}
.wm{font-weight:700;color:#fff}
table{border-collapse:collapse;font-size:5.5px;color:var(--ink)}
td,th{border-bottom:1px solid var(--line);padding:3px 5px;text-align:left}
th{background:var(--blue);color:#fff;font-weight:600}
</style>
</head>
<body>
<main class="deck">

<!-- row 1 -->
<section class="slide green">
  <div class="ph" role="img" aria-label="Physician portrait" style="left:200px;top:0;width:192px;height:220px;background:linear-gradient(135deg,#dfe8ec,#b9c9d2)"></div>
  <div class="abs wm" style="left:22px;top:70px;font-size:40px">Traloma</div>
  <p class="abs p white" style="left:24px;top:124px;font-size:8px">Medical device presentation</p>
</section>
<section class="slide">
  <div class="ph" role="img" aria-label="Medical team at work" style="left:0;top:0;width:392px;height:140px"></div>
  <div class="panel" style="left:0;top:140px;width:392px;height:80px"></div>
  <div class="abs wm" style="left:120px;top:162px;font-size:14px">Your Title Goes Here</div>
  <p class="abs p white" style="left:120px;top:184px">Short subtitle for this slide</p>
  <span class="logo light">Traloma</span>
</section>
<section class="slide">
  <div class="abs" style="left:16px;top:12px;font-size:18px;font-weight:700;color:var(--green)">Traloma</div>
  <div class="ph" role="img" aria-label="Surgeons in operating room" style="left:0;top:44px;width:392px;height:110px"></div>
  <div class="hd" style="top:170px;left:auto;right:20px">Your Title Goes Here</div>
  <p class="abs p" style="right:20px;top:192px">Short subtitle text</p>
  <div class="foot"></div>
</section>

<!-- row 2 -->
<section class="slide">
  <div class="abs" style="left:20px;top:40px;width:140px;height:140px;border-radius:50%;border:6px solid var(--green)"></div>
  <h2 class="hd" style="left:44px;top:88px;font-size:12px">Your Title<br>Goes Here</h2>
  <p class="abs p" style="left:44px;top:124px">Phone 555 0100</p>
  <div class="ph" role="img" aria-label="Doctor with clipboard" style="left:196px;top:0;width:196px;height:220px"></div>
  <div class="foot"></div>
</section>
<section class="slide green">
  <div class="circle" style="left:176px;top:40px;width:40px;height:40px;background:#fff"></div>
  <div class="abs" style="left:187px;top:44px;font-size:26px;font-weight:700;color:var(--green)">“</div>
  <p class="abs p white" style="left:70px;top:96px;width:252px;text-align:center;font-size:9px">Clean care begins with gentle and precise treatment for every patient we serve.</p>
  <span class="logo light">Traloma</span>
</section>
<section class="slide">
  <h2 class="hd">Our Agenda</h2><span class="logo">Traloma</span>
  <div class="chip" style="left:30px;top:56px"></div><p class="abs p" style="left:50px;top:58px">Agenda item one</p>
  <div class="chip" style="left:30px;top:96px"></div><p class="abs p" style="left:50px;top:98px">Agenda item two</p>
  <div class="chip" style="left:30px;top:136px"></div><p class="abs p" style="left:50px;top:138px">Agenda item three</p>
  <div class="chip" style="left:210px;top:56px"></div><p class="abs p" style="left:230px;top:58px">Agenda item four</p>
  <div class="chip" style="left:210px;top:96px"></div><p class="abs p" style="left:230px;top:98px">Agenda item five</p>
  <div class="chip" style="left:210px;top:136px"></div><p class="abs p" style="left:230px;top:138px">Agenda item six</p>
  <div class="foot"></div>
</section>

<!-- row 3 -->
<section class="slide">
  <div class="ph" role="img" aria-label="Hands typing on laptop" style="left:0;top:0;width:200px;height:220px"></div>
  <div class="panel" style="left:200px;top:0;width:192px;height:220px"></div>
  <h2 class="hd white" style="left:218px;top:40px">About Us</h2>
  <p class="abs p white" style="left:218px;top:66px;width:150px">We develop an ultrasound catheter for the treatment of hypertension.</p>
  <span class="logo light">Traloma</span>
</section>
<section class="slide">
  <h2 class="hd">Our Services</h2><span class="logo">Traloma</span>
  <div class="ph" role="img" aria-label="Clinicians consulting" style="left:20px;top:50px;width:108px;height:80px"></div>
  <div class="ph" role="img" aria-label="Doctor with patient" style="left:142px;top:50px;width:108px;height:80px"></div>
  <div class="ph" role="img" aria-label="Lab researcher" style="left:264px;top:50px;width:108px;height:80px"></div>
  <p class="abs sub blue" style="left:20px;top:140px">Service One</p><p class="abs p" style="left:20px;top:154px;width:108px">Brief service detail text</p>
  <p class="abs sub blue" style="left:142px;top:140px">Service Two</p><p class="abs p" style="left:142px;top:154px;width:108px">Brief service detail text</p>
  <p class="abs sub blue" style="left:264px;top:140px">Service Three</p><p class="abs p" style="left:264px;top:154px;width:108px">Brief service detail text</p>
  <div class="foot"></div>
</section>
<section class="slide">
  <h2 class="hd">Quote Area</h2><span class="logo">Traloma</span>
  <div class="abs" style="left:20px;top:50px;font-size:30px;font-weight:700;color:var(--green)">“</div>
  <p class="abs p" style="left:20px;top:86px;width:170px;font-size:7px">Our goal is safer and simpler care for patients with high blood pressure.</p>
  <div class="ph" role="img" aria-label="Nurse portrait" style="left:220px;top:40px;width:172px;height:180px"></div>
  <div class="foot"></div>
</section>

<!-- row 4 -->
<section class="slide">
  <h2 class="hd">Text Area</h2><span class="logo">Traloma</span>
  <p class="abs sub" style="left:16px;top:48px">Welcome to Our<br>Technology in Modern Care</p>
  <p class="abs p" style="left:16px;top:80px;width:360px">Short body text describing the technology and its benefits for patients and clinicians in daily practice.</p>
  <p class="abs p" style="left:16px;top:112px;width:360px">Second paragraph with a few more supporting details about the device.</p>
  <div class="foot"></div>
</section>
<section class="slide green">
  <h2 class="hd white">Our Vision &amp; Mission</h2><span class="logo light">Traloma</span>
  <div class="abs" style="left:16px;top:60px;width:110px;height:120px;background:rgba(255,255,255,.18)"></div>
  <p class="abs sub" style="left:24px;top:70px;color:#fff">Vision</p><p class="abs p white" style="left:24px;top:86px;width:94px">Short vision text here</p>
  <div class="ph" role="img" aria-label="Doctors discussing" style="left:140px;top:60px;width:236px;height:120px"></div>
</section>
<section class="slide">
  <div class="abs" style="left:0;top:0;width:392px;height:56px;background:var(--blue)"></div>
  <h2 class="hd white">Text Area</h2><span class="logo light">Traloma</span>
  <p class="abs sub" style="left:16px;top:70px">Welcome to Our<br>Technology in Modern Care</p>
  <p class="abs p" style="left:16px;top:102px;width:360px">Short body text describing the technology and its benefits for patients and clinicians.</p>
  <div class="foot"></div>
</section>

<!-- row 5 -->
<section class="slide">
  <div class="ph g" role="img" aria-label="Hand holding device" style="left:0;top:0;width:230px;height:220px"></div>
  <div class="abs wm" style="left:24px;top:86px;font-size:28px">Traloma</div>
  <h2 class="hd" style="left:246px;top:80px;font-size:12px">Your Title Goes Here</h2>
  <p class="abs p" style="left:246px;top:102px;width:130px">Short supporting line</p>
</section>
<section class="slide">
  <h2 class="hd">Your Title Goes Here</h2><span class="logo">Traloma</span>
  <div class="ph" role="img" aria-label="Doctor at desk" style="left:16px;top:50px;width:170px;height:140px"></div>
  <p class="abs li" style="left:206px;top:60px">List point one</p>
  <p class="abs li" style="left:206px;top:86px">List point two</p>
  <p class="abs li" style="left:206px;top:112px">List point three</p>
  <p class="abs li" style="left:206px;top:138px">List point four</p>
  <div class="foot"></div>
</section>
<section class="slide">
  <div class="ph" role="img" aria-label="Surgeon in mask" style="left:0;top:0;width:200px;height:220px"></div>
  <div class="panel" style="left:200px;top:0;width:192px;height:220px;background:var(--blue)"></div>
  <p class="abs sub" style="left:216px;top:28px;color:#fff">We are here to<br>help every patient</p>
  <p class="abs li" style="left:216px;top:70px;color:#fff">Point one</p>
  <p class="abs li" style="left:216px;top:96px;color:#fff">Point two</p>
  <p class="abs li" style="left:216px;top:122px;color:#fff">Point three</p>
  <p class="abs li" style="left:216px;top:148px;color:#fff">Point four</p>
</section>

<!-- row 6 -->
<section class="slide">
  <div class="circle" style="left:-30px;top:40px;width:150px;height:150px;background:var(--green)"></div>
  <div class="abs wm" style="left:14px;top:104px;font-size:18px">Traloma</div>
  <div class="ph" role="img" aria-label="Smiling doctor" style="left:140px;top:0;width:252px;height:150px"></div>
  <div class="ph" role="img" aria-label="Medical team" style="left:140px;top:156px;width:252px;height:64px"></div>
</section>
<section class="slide">
  <h2 class="hd">Your Title Goes Here</h2><span class="logo">Traloma</span>
  <p class="abs sub" style="left:16px;top:50px">Welcome to Our<br>Technology</p>
  <p class="abs p" style="left:16px;top:80px;width:150px">Short body text about the approach and its results.</p>
  <div class="ph" role="img" aria-label="Clinic scene" style="left:186px;top:50px;width:90px;height:70px"></div>
  <div class="ph" role="img" aria-label="Doctor portrait" style="left:284px;top:50px;width:90px;height:70px"></div>
  <div class="ph" role="img" aria-label="Patient care" style="left:186px;top:126px;width:188px;height:70px"></div>
  <div class="foot"></div>
</section>
<section class="slide">
  <h2 class="hd">Portfolio Area</h2><span class="logo">Traloma</span>
  <p class="abs li" style="left:16px;top:60px">Project one</p>
  <p class="abs li" style="left:16px;top:86px">Project two</p>
  <p class="abs li" style="left:16px;top:112px">Project three</p>
  <p class="abs li" style="left:16px;top:138px">Project four</p>
  <div class="ph" role="img" aria-label="Doctor at work" style="left:150px;top:46px;width:110px;height:150px"></div>
  <div class="ph" role="img" aria-label="Scrubs team" style="left:266px;top:46px;width:110px;height:72px"></div>
  <div class="ph" role="img" aria-label="Lab detail" style="left:266px;top:124px;width:110px;height:72px"></div>
  <div class="foot"></div>
</section>

<!-- row 7 -->
<section class="slide">
  <h2 class="hd">Your Title Goes Here</h2><span class="logo">Traloma</span>
  <div class="ph" role="img" aria-label="Catheter console device" style="left:130px;top:60px;width:130px;height:90px;background:linear-gradient(135deg,#5b6a77,#1d2730)"></div>
  <p class="abs li" style="left:16px;top:70px">Feature one</p>
  <p class="abs li" style="left:16px;top:100px">Feature two</p>
  <p class="abs li" style="left:280px;top:70px">Feature three</p>
  <p class="abs li" style="left:280px;top:100px">Feature four</p>
  <div class="foot"></div>
</section>
<section class="slide">
  <h2 class="hd">Our Differences</h2><span class="logo">Traloma</span>
  <div class="ph" role="img" aria-label="Surgery team" style="left:16px;top:48px;width:175px;height:92px"></div>
  <div class="ph" role="img" aria-label="Clinician with tablet" style="left:201px;top:48px;width:175px;height:92px"></div>
  <p class="abs p" style="left:16px;top:150px;width:175px">Short point on what sets us apart</p>
  <p class="abs p" style="left:201px;top:150px;width:175px">Short point on what sets us apart</p>
  <div class="foot"></div>
</section>
<section class="slide">
  <h2 class="hd">Your Title Goes Here</h2><span class="logo">Traloma</span>
  <p class="abs li" style="left:16px;top:60px">Detail one</p>
  <p class="abs li" style="left:16px;top:86px">Detail two</p>
  <p class="abs li" style="left:16px;top:112px">Detail three</p>
  <div class="ph" role="img" aria-label="Doctor portrait" style="left:210px;top:0;width:182px;height:220px"></div>
</section>

<!-- row 8 -->
<section class="slide">
  <h2 class="hd">Two Column Description</h2><span class="logo">Traloma</span>
  <p class="abs sub" style="left:16px;top:50px">Welcome to Our Technology</p>
  <p class="abs p" style="left:16px;top:70px;width:170px">Short column text about the product and its clinical value.</p>
  <p class="abs p" style="left:206px;top:70px;width:170px">Short column text about the team and its clinical vision.</p>
  <div class="foot"></div>
</section>
<section class="slide green" style="background:linear-gradient(135deg,#7fbb3a,#4f8f22)">
  <div class="abs" style="left:170px;top:80px;width:52px;height:52px;border-radius:50%;background:#fff"></div>
  <div class="abs wm" style="left:0;right:0;top:140px;text-align:center;font-size:14px">Traloma</div>
</section>
<section class="slide">
  <h2 class="hd">Three Column Description</h2><span class="logo">Traloma</span>
  <p class="abs sub" style="left:16px;top:50px">Welcome to Our Technology</p>
  <p class="abs p" style="left:16px;top:70px;width:110px">Short column text one here.</p>
  <p class="abs p" style="left:141px;top:70px;width:110px">Short column text two here.</p>
  <p class="abs p" style="left:266px;top:70px;width:110px">Short column text three here.</p>
  <div class="foot"></div>
</section>

<!-- row 9 -->
<section class="slide">
  <div class="ph g" role="img" aria-label="Doctor with tablet, green tint" style="left:0;top:0;width:392px;height:220px"></div>
  <div class="circle" style="left:200px;top:60px;width:44px;height:44px;background:rgba(255,255,255,.35)"></div>
  <div class="circle" style="left:256px;top:60px;width:44px;height:44px;background:rgba(255,255,255,.35)"></div>
  <div class="circle" style="left:312px;top:60px;width:44px;height:44px;background:rgba(255,255,255,.35)"></div>
  <span class="logo light">Traloma</span>
</section>
<section class="slide">
  <h2 class="hd">Your Title Goes Here</h2><span class="logo">Traloma</span>
  <div class="ph" role="img" aria-label="Doctor portrait" style="left:16px;top:48px;width:130px;height:150px"></div>
  <div class="abs" style="left:160px;top:56px;width:216px;height:26px;background:var(--blue)"></div>
  <div class="abs" style="left:160px;top:90px;width:216px;height:26px;background:var(--green)"></div>
  <div class="abs" style="left:160px;top:124px;width:216px;height:26px;background:var(--blue)"></div>
  <div class="abs" style="left:160px;top:158px;width:216px;height:26px;background:var(--green)"></div>
  <div class="foot"></div>
</section>
<section class="slide">
  <div class="ph" role="img" aria-label="Clinician smiling" style="left:0;top:0;width:180px;height:220px"></div>
  <h2 class="hd" style="left:196px;top:40px">Your Title<br>Goes Here</h2><span class="logo">Traloma</span>
  <p class="abs p" style="left:196px;top:90px;width:180px">Short supporting text for this layout.</p>
  <div class="foot"></div>
</section>

<!-- row 10 -->
<section class="slide">
  <h2 class="hd">Four Bullets with Paragraph</h2><span class="logo">Traloma</span>
  <div class="circle" style="left:20px;top:60px;width:20px;height:20px;background:var(--green)"></div><p class="abs p" style="left:48px;top:64px">Bullet text one</p>
  <div class="circle" style="left:200px;top:60px;width:20px;height:20px"></div><p class="abs p" style="left:228px;top:64px">Bullet text two</p>
  <div class="circle" style="left:20px;top:120px;width:20px;height:20px"></div><p class="abs p" style="left:48px;top:124px">Bullet text three</p>
  <div class="circle" style="left:200px;top:120px;width:20px;height:20px;background:var(--green)"></div><p class="abs p" style="left:228px;top:124px">Bullet text four</p>
  <div class="foot"></div>
</section>
<section class="slide">
  <h2 class="hd">Your Title</h2><span class="logo">Traloma</span>
  <div class="ph" role="img" aria-label="Doctor standing" style="left:146px;top:40px;width:100px;height:180px"></div>
  <p class="abs li" style="left:16px;top:70px">Item one</p><p class="abs li" style="left:16px;top:110px">Item two</p>
  <p class="abs li blue" style="left:270px;top:70px">Item three</p><p class="abs li blue" style="left:270px;top:110px">Item four</p>
</section>
<section class="slide">
  <h2 class="hd">Text &amp; Bullet Area</h2><span class="logo">Traloma</span>
  <p class="abs p" style="left:16px;top:50px;width:360px">Short introduction text placed above the bullets.</p>
  <p class="abs li" style="left:16px;top:80px">Bullet one</p><p class="abs li blue" style="left:206px;top:80px">Bullet two</p>
  <p class="abs li blue" style="left:16px;top:116px">Bullet three</p><p class="abs li" style="left:206px;top:116px">Bullet four</p>
  <p class="abs li" style="left:16px;top:152px">Bullet five</p><p class="abs li blue" style="left:206px;top:152px">Bullet six</p>
  <div class="foot"></div>
</section>

<!-- row 11 -->
<section class="slide">
  <h2 class="hd">Pictures with Bullets</h2><span class="logo">Traloma</span>
  <div class="ph" role="img" aria-label="Clinical team" style="left:16px;top:48px;width:112px;height:80px"></div>
  <div class="ph" role="img" aria-label="Doctor and patient" style="left:140px;top:48px;width:112px;height:80px"></div>
  <div class="ph" role="img" aria-label="Lab work" style="left:264px;top:48px;width:112px;height:80px"></div>
  <p class="abs li" style="left:16px;top:144px">Point one</p><p class="abs li" style="left:140px;top:144px">Point two</p><p class="abs li" style="left:264px;top:144px">Point three</p>
  <div class="foot"></div>
</section>
<section class="slide green">
  <span class="logo light">Traloma</span>
  <h2 class="hd white" style="left:0;right:0;top:96px;text-align:center">Your Title Goes Here</h2>
</section>
<section class="slide">
  <h2 class="hd">Your Title Goes Here</h2><span class="logo">Traloma</span>
  <div class="ph" role="img" aria-label="Doctor portrait" style="left:16px;top:48px;width:116px;height:76px"></div>
  <div class="ph" role="img" aria-label="Consultation" style="left:138px;top:48px;width:116px;height:76px"></div>
  <div class="ph" role="img" aria-label="Surgery" style="left:260px;top:48px;width:116px;height:76px"></div>
  <div class="ph" role="img" aria-label="Nurse at work" style="left:16px;top:130px;width:116px;height:76px"></div>
  <div class="ph" role="img" aria-label="Team meeting" style="left:138px;top:130px;width:116px;height:76px"></div>
  <div class="ph" role="img" aria-label="Research lab" style="left:260px;top:130px;width:116px;height:76px"></div>
</section>

<!-- row 12 -->
<section class="slide">
  <h2 class="hd">Paragraph with Three Bullet</h2><span class="logo">Traloma</span>
  <p class="abs sub" style="left:16px;top:50px">Welcome to Our Technology</p>
  <p class="abs p" style="left:16px;top:68px;width:360px">Short paragraph introducing the three key points below.</p>
  <p class="abs li" style="left:16px;top:104px">Key point one</p><p class="abs li" style="left:16px;top:130px">Key point two</p><p class="abs li" style="left:16px;top:156px">Key point three</p>
  <div class="foot"></div>
</section>
<section class="slide">
  <h2 class="hd">Global Experience</h2><span class="logo">Traloma</span>
  <div class="ph" role="img" aria-label="World map with locations" style="left:40px;top:48px;width:312px;height:150px;background:linear-gradient(135deg,#e3e8ec,#c4ced6)"></div>
</section>
<section class="slide">
  <h2 class="hd">Multiple Column Area</h2><span class="logo">Traloma</span>
  <div class="circle" style="left:36px;top:60px;width:30px;height:30px;background:var(--green)"></div>
  <div class="circle" style="left:126px;top:60px;width:30px;height:30px"></div>
  <div class="circle" style="left:216px;top:60px;width:30px;height:30px;background:var(--green)"></div>
  <div class="circle" style="left:306px;top:60px;width:30px;height:30px"></div>
  <p class="abs p" style="left:20px;top:102px;width:64px;text-align:center">Column one</p>
  <p class="abs p" style="left:110px;top:102px;width:64px;text-align:center">Column two</p>
  <p class="abs p" style="left:200px;top:102px;width:64px;text-align:center">Column three</p>
  <p class="abs p" style="left:290px;top:102px;width:64px;text-align:center">Column four</p>
  <div class="foot"></div>
</section>

<!-- row 13 -->
<section class="slide green">
  <span class="logo light">Traloma</span>
  <div class="ph" role="img" aria-label="Surgeon portrait" style="left:16px;top:40px;width:160px;height:140px"></div>
  <h2 class="hd white" style="left:196px;top:80px">Your Title Goes Here</h2>
  <p class="abs p white" style="left:196px;top:104px">Short subtitle text</p>
</section>
<section class="slide green">
  <span class="logo light">Traloma</span>
  <div class="ph g" role="img" aria-label="Faint clinic background" style="left:0;top:0;width:392px;height:220px;opacity:.6"></div>
</section>
<section class="slide">
  <h2 class="hd" style="top:60px">Video Title<br>Goes Here</h2><span class="logo">Traloma</span>
  <p class="abs p" style="left:16px;top:106px;width:140px">Short video description</p>
  <svg class="abs" style="left:180px;top:40px" width="196" height="150" viewBox="0 0 196 150">
    <rect x="2" y="2" width="192" height="116" rx="4" fill="#2b2f33"/>
    <rect x="8" y="8" width="180" height="104" fill="#c9d6de"/>
    <path d="M88 44 L112 60 L88 76 Z" fill="#fff"/>
    <rect x="84" y="118" width="28" height="20" fill="#9aa3a9"/>
    <rect x="64" y="138" width="68" height="6" rx="2" fill="#9aa3a9"/>
  </svg>
</section>

<!-- row 14 -->
<section class="slide">
  <h2 class="hd">Four Column Area</h2><span class="logo">Traloma</span>
  <div class="abs" style="left:16px;top:52px;width:82px;height:70px;background:var(--blue)"></div>
  <div class="abs" style="left:108px;top:52px;width:82px;height:70px;background:var(--blue-d)"></div>
  <div class="abs" style="left:200px;top:52px;width:82px;height:70px;background:var(--blue)"></div>
  <div class="abs" style="left:292px;top:52px;width:82px;height:70px;background:var(--blue-d)"></div>
  <p class="abs p" style="left:16px;top:132px;width:82px">Column text one</p><p class="abs p" style="left:108px;top:132px;width:82px">Column text two</p>
  <p class="abs p" style="left:200px;top:132px;width:82px">Column text three</p><p class="abs p" style="left:292px;top:132px;width:82px">Column text four</p>
  <div class="foot"></div>
</section>
<section class="slide">
  <h2 class="hd">Four Column Area</h2><span class="logo">Traloma</span>
  <div class="circle" style="left:36px;top:58px;width:40px;height:40px;background:none;border:3px solid var(--green)"></div>
  <div class="circle" style="left:128px;top:58px;width:40px;height:40px;background:none;border:3px solid var(--blue)"></div>
  <div class="circle" style="left:220px;top:58px;width:40px;height:40px;background:none;border:3px solid var(--green)"></div>
  <div class="circle" style="left:312px;top:58px;width:40px;height:40px;background:none;border:3px solid var(--blue)"></div>
  <p class="abs p" style="left:20px;top:112px;width:72px;text-align:center">Text one</p><p class="abs p" style="left:112px;top:112px;width:72px;text-align:center">Text two</p>
  <p class="abs p" style="left:204px;top:112px;width:72px;text-align:center">Text three</p><p class="abs p" style="left:296px;top:112px;width:72px;text-align:center">Text four</p>
  <div class="foot"></div>
</section>
<section class="slide">
  <h2 class="hd">Key Points Area</h2><span class="logo">Traloma</span>
  <div class="circle" style="left:166px;top:70px;width:60px;height:60px;background:var(--green)"></div>
  <p class="abs li" style="left:40px;top:60px">Point one</p><p class="abs li" style="left:40px;top:130px">Point two</p>
  <p class="abs li blue" style="left:270px;top:60px">Point three</p><p class="abs li blue" style="left:270px;top:130px">Point four</p>
  <div class="foot"></div>
</section>

<!-- row 15 -->
<section class="slide">
  <h2 class="hd">Process Area</h2><span class="logo">Traloma</span>
  <svg class="abs" style="left:16px;top:70px" width="360" height="60" viewBox="0 0 360 60">
    <g fill="#1b96d3"><rect x="0" y="14" width="70" height="32" rx="3"/><rect x="96" y="14" width="70" height="32" rx="3"/><rect x="192" y="14" width="70" height="32" rx="3"/></g>
    <rect x="288" y="14" width="70" height="32" rx="3" fill="#8cc63f"/>
    <g stroke="#8d8d8d" stroke-width="2" fill="none"><path d="M72 30h20M168 30h20M264 30h20"/></g>
    <g fill="#8d8d8d"><path d="M92 26l4 4-4 4zM188 26l4 4-4 4zM284 26l4 4-4 4z"/></g>
  </svg>
  <div class="foot"></div>
</section>
<section class="slide">
  <h2 class="hd">Workflow Area</h2><span class="logo">Traloma</span>
  <svg class="abs" style="left:16px;top:60px" width="360" height="110" viewBox="0 0 360 110">
    <path d="M0 55 C45 5 75 5 120 55 S195 105 240 55 S315 5 360 55" fill="none" stroke="#1b96d3" stroke-width="10"/>
    <g fill="#8cc63f"><circle cx="60" cy="30" r="12"/><circle cx="180" cy="80" r="12"/><circle cx="300" cy="30" r="12"/></g>
  </svg>
  <div class="foot"></div>
</section>
<section class="slide">
  <h2 class="hd">Timeline</h2><span class="logo">Traloma</span>
  <div class="abs" style="left:30px;top:108px;width:332px;height:3px;background:var(--line)"></div>
  <div class="circle" style="left:36px;top:90px;width:38px;height:38px"></div>
  <div class="circle" style="left:130px;top:90px;width:38px;height:38px;background:#cfd6dc"></div>
  <div class="circle" style="left:224px;top:90px;width:38px;height:38px"></div>
  <div class="circle" style="left:318px;top:90px;width:38px;height:38px;background:#cfd6dc"></div>
  <p class="abs p" style="left:36px;top:140px">2019</p><p class="abs p" style="left:130px;top:140px">2020</p><p class="abs p" style="left:224px;top:140px">2021</p><p class="abs p" style="left:318px;top:140px">2022</p>
  <div class="foot"></div>
</section>

<!-- row 16 -->
<section class="slide">
  <h2 class="hd">Bullet &amp; Chart Area</h2><span class="logo">Traloma</span>
  <svg class="abs" style="left:16px;top:54px" width="210" height="130" viewBox="0 0 210 130">
    <g fill="#1b96d3"><rect x="0" y="4" width="170" height="12"/><rect x="0" y="58" width="150" height="12"/><rect x="0" y="112" width="120" height="12"/></g>
    <g fill="#8cc63f"><rect x="0" y="22" width="130" height="12"/><rect x="0" y="76" width="190" height="12"/></g>
  </svg>
  <p class="abs li" style="left:250px;top:70px">Bullet one</p><p class="abs li blue" style="left:250px;top:100px">Bullet two</p><p class="abs li" style="left:250px;top:130px">Bullet three</p>
  <div class="foot"></div>
</section>
<section class="slide">
  <h2 class="hd">Table Area</h2><span class="logo">Traloma</span>
  <table class="abs" style="left:40px;top:48px;width:312px">
    <tr><th>Item</th><th>Basic</th><th>Plus</th><th>Pro</th></tr>
    <tr><td>Feature A</td><td>Yes</td><td>Yes</td><td>Yes</td></tr>
    <tr><td>Feature B</td><td>No</td><td>Yes</td><td>Yes</td></tr>
    <tr><td>Feature C</td><td>No</td><td>No</td><td>Yes</td></tr>
    <tr><td>Feature D</td><td>No</td><td>Yes</td><td>Yes</td></tr>
  </table>
</section>
<section class="slide">
  <h2 class="hd">Bullet &amp; Chart Area</h2><span class="logo">Traloma</span>
  <p class="abs li" style="left:16px;top:70px">Bullet one</p><p class="abs li blue" style="left:16px;top:100px">Bullet two</p><p class="abs li" style="left:16px;top:130px">Bullet three</p>
  <svg class="abs" style="left:220px;top:52px" width="130" height="130" viewBox="0 0 36 36">
    <circle cx="18" cy="18" r="14" fill="none" stroke="#e3e8ec" stroke-width="6"/>
    <circle cx="18" cy="18" r="14" fill="none" stroke="#1b96d3" stroke-width="6" stroke-dasharray="55 88" transform="rotate(-90 18 18)"/>
    <circle cx="18" cy="18" r="14" fill="none" stroke="#8cc63f" stroke-width="6" stroke-dasharray="20 88" stroke-dashoffset="-55" transform="rotate(-90 18 18)"/>
  </svg>
  <div class="foot"></div>
</section>

<!-- row 17 -->
<section class="slide">
  <h2 class="hd">Pricing Structure</h2><span class="logo">Traloma</span>
  <table class="abs" style="left:16px;top:48px;width:360px">
    <tr><th>Choose Plan</th><th>Basic</th><th>Plus</th><th>Pro</th></tr>
    <tr><td>Option one</td><td>$10</td><td>$20</td><td>$30</td></tr>
    <tr><td>Option two</td><td>$15</td><td>$25</td><td>$35</td></tr>
    <tr><td>Option three</td><td>$20</td><td>$30</td><td>$40</td></tr>
    <tr><td>Option four</td><td>$25</td><td>$35</td><td>$45</td></tr>
  </table>
</section>
<section class="slide">
  <div class="ph" role="img" aria-label="Doctor standing" style="left:0;top:0;width:150px;height:220px"></div>
  <span class="logo">Traloma</span>
  <div class="ph round" role="img" aria-label="Team member photo" style="left:180px;top:40px;width:50px;height:50px"></div>
  <div class="ph round" role="img" aria-label="Team member photo" style="left:290px;top:40px;width:50px;height:50px"></div>
  <div class="ph round" role="img" aria-label="Team member photo" style="left:180px;top:120px;width:50px;height:50px"></div>
  <div class="ph round" role="img" aria-label="Team member photo" style="left:290px;top:120px;width:50px;height:50px"></div>
  <p class="abs cap" style="left:170px;top:92px;width:70px">Team Name</p><p class="abs cap" style="left:280px;top:92px;width:70px">Team Name</p>
  <p class="abs cap" style="left:170px;top:172px;width:70px">Team Name</p><p class="abs cap" style="left:280px;top:172px;width:70px">Team Name</p>
</section>
<section class="slide">
  <div class="ph g" role="img" aria-label="Clinic corridor, green tint" style="left:0;top:0;width:392px;height:220px"></div>
  <div class="abs wm" style="left:24px;top:24px;font-size:22px">Traloma</div>
  <h2 class="hd white" style="left:24px;top:150px">Our Contact</h2>
  <p class="abs p white" style="left:24px;top:172px">hello@traloma.example · 555 0100</p>
</section>

</main>
</body>
</html>
```